Telmoro Business Card

I already have the conplay logo. I need to develop a professional business card layout

Target Market(s)

Business

Industry/Entity Type

Business

Contact Information for Business Card

Company Name: Telmoro Limited

Font styles to use
Sans Serif

Colors

Designer to choose colors to be used in the design.

Requirements
Must have
• Use current logo
• Need two card size options:
• Small Card: 70mm x 28mm (Landscape)
• Square Card: 65mm x 65mm
Nice to have
• I will need 8-10 files for each name, number and email address (details to follow)

```html
<!DOCTYPE html>
<html lang="en">
<head>
<meta charset="utf-8">
<title>Telmoro Business Card</title>
<link rel="stylesheet" href="https://fonts.googleapis.com/css2?family=Lato:wght@400;700;900&display=swap">
<style>
  :root {
    --canvas: #ebebeb;
    --card-dark: #050505;
    --card-light: #ffffff;
    --ink: #1a1a1a;
    --brand: #ffffff;
    --band-blue: #2a7de1;
    --band-yellow: #ffd200;
    --band-red: #e3101b;
    --band-orange: #f08a0c;
    --band-green: #7cc21d;
  }
  * { box-sizing: border-box; margin: 0; padding: 0; }
  html, body {
    width: 1200px;
    height: 954px;
    overflow: hidden;
    background: var(--canvas);
    font-family: "Lato", sans-serif;
  }
  .sheet {
    position: relative;
    width: 1200px;
    height: 954px;
  }
  .card {
    position: absolute;
    overflow: hidden;
    box-shadow: 0 10px 30px rgba(0,0,0,0.18);
  }
  /* Small card 70 x 28 mm (2.5 : 1) */
  .card--landscape { left: 70px; width: 600px; height: 240px; }
  .card--landscape.card--front { top: 167px; }
  .card--landscape.card--back { top: 547px; }
  /* Square card 65 x 65 mm */
  .card--square { left: 790px; width: 320px; height: 320px; }
  .card--square.card--front { top: 127px; }
  .card--square.card--back { top: 507px; }

  .card--front {
    background: var(--card-dark);
    display: flex;
    align-items: center;
    justify-content: center;
  }
  .brand-name {
    color: var(--brand);
    font-weight: 900;
    letter-spacing: 2px;
    text-transform: uppercase;
    line-height: 1;
  }
  .card--landscape .brand-name { font-size: 80px; }
  .card--square .brand-name { font-size: 48px; letter-spacing: 1px; }

  .card--back {
    background: var(--card-light);
    color: var(--ink);
    display: flex;
    align-items: center;
    justify-content: center;
    text-align: center;
  }
  .card--landscape.card--back { padding-bottom: 10px; }
  .card--square.card--back { padding-bottom: 12px; }
  .contact__name {
    font-weight: 700;
    letter-spacing: 0.5px;
    text-transform: uppercase;
    line-height: 1.1;
  }
  .contact__role {
    font-weight: 700;
    letter-spacing: 1px;
    text-transform: uppercase;
    margin-top: 4px;
  }
  .contact__details {
    list-style: none;
    line-height: 1.4;
  }
  .card--landscape .contact__name { font-size: 26px; }
  .card--landscape .contact__role { font-size: 9px; }
  .card--landscape .contact__details { font-size: 14px; margin-top: 12px; }
  .card--square .contact__name { font-size: 28px; }
  .card--square .contact__role { font-size: 10px; }
  .card--square .contact__details { font-size: 15px; margin-top: 16px; }

  .color-band {
    position: absolute;
    left: 0;
    right: 0;
    bottom: 0;
    display: flex;
  }
  .card--landscape .color-band { height: 10px; }
  .card--square .color-band { height: 12px; }
  .color-band span { flex: 1; }
  .color-band .blue { background: var(--band-blue); }
  .color-band .yellow { background: var(--band-yellow); }
  .color-band .red { background: var(--band-red); }
  .color-band .orange { background: var(--band-orange); }
  .color-band .green { background: var(--band-green); }
</style>
</head>
<body>
  <main class="sheet">
    <section class="card card--landscape card--front" aria-label="Small card front">
      <div class="brand-name">Telmoro</div>
    </section>

    <section class="card card--landscape card--back" aria-label="Small card back">
      <div class="contact">
        <h1 class="contact__name">Alan Rivers</h1>
        <p class="contact__role">Managing Director</p>
        <ul class="contact__details">
          <li>48 Harbor Lane, Westfield CO 5821</li>
          <li>0044 517 2846</li>
          <li>info@telmoro.com</li>
          <li>www.telmoro.com</li>
        </ul>
      </div>
      <div class="color-band">
        <span class="blue"></span><span class="yellow"></span><span class="red"></span><span class="orange"></span><span class="green"></span>
      </div>
    </section>

    <section class="card card--square card--front" aria-label="Square card front">
      <div class="brand-name">Telmoro</div>
    </section>

    <section class="card card--square card--back" aria-label="Square card back">
      <div class="contact">
        <h2 class="contact__name">Alan Rivers</h2>
        <p class="contact__role">Managing Director</p>
        <ul class="contact__details">
          <li>48 Harbor Lane, Westfield CO 5821</li>
          <li>0044 517 2846</li>
          <li>info@telmoro.com</li>
          <li>www.telmoro.com</li>
        </ul>
      </div>
      <div class="color-band">
        <span class="blue"></span><span class="yellow"></span><span class="red"></span><span class="orange"></span><span class="green"></span>
      </div>
    </section>
  </main>
</body>
</html>
```